Two Versions of a Business Card for a Lawyer

Summary: I need a logo and a business card. The business card is two-sided and comes in two versions. One version is conservative, the other is slightly different with one or more pink embellishments in the logo or somewhere else in the business card.
I'm about to start off as a sole practitioner in criminal and immigration law. I'll largely be working with marginalised communities and in areas of social justice. One of my main focuses will be gendered violence, I'm hoping to specialise my practice towards representing victims of domestic and sexual violence and sex workers. I want a business card which would attract this clientele and make them feel safe to speak with me. I'd also like it to communicate a sense of hope.
However, the business card still has to be very conservative as the legal profession is very stuffy. So I was thinking of having two versions of the same card, one would be very straight forward while the other would have a **pink embellishment** or perhaps several. For example, if the scales of justice were used in the design, maybe the second version would have a pink flower about to bloom on the scale somewhere. Or maybe it's my logo that is different and pink.
While both designs have to be pretty conservative, I still want it to give off a sense that I'm alternative and think outside the box. With lawyers, I think a little bit of deviation goes a long way (less is more).
As far as colour goes (other than the pink embellishment), I was thinking something monochromatic, probably black and white but I am open to considering more colours. I personally love colour, and would love to use more colour, but am hesitant because of the nature of the profession. If you can find a way to use more colour while keeping it conservative and letting the pink pop, I'd be pretty pleased.
In general, I would prefer a clean simplistic design and logo. It should be immediately obvious that I'm a lawyer just by glancing at the card. I'm open to symbols of law, like the scales of justice or lady justice or something else. However, I don't want it to be the same as everyone else's.
Eventually, the design/style should be easy to recreate in the form of a website.
As far as the logo goes, it would probably use a circle as my last name starts with the letter "O". It can be very simple, with just my name and "Barrister & Solicitor". I don't currently have a logo, but the winning designer will be invited to provide a separate file for just the logo for an additional fee (I think it was CA$99). (Please ignore the uploaded logo file, it just wouldn't let me continue without uploading something).
As for the information that should go into the card, I'm still finalizing my address and phone number. So please use a placeholder for now.
Target Market(s)
Women, victims of sexual or domestic violence, refugees, people in need of legal services
Industry/Entity Type
Lawyer
Contact Information for Business Card
Maren Vickery
Barrister & Solicitor
LL.B., B.C.L., B.F.A.
Criminal & Immigration Law
Street address
Toronto, ON
Postal Code
Phone number
Fax number
Email
Logo Text
Maren Vickery, Barrister & Solicitor
Requirements
Must have
- Two versions
- One with pink
- Simplistic
Nice to have
- Maybe more colour
Should not have
- Not too conservative
- Not too predictable

```html
<!DOCTYPE html>
<html lang="en">
<head>
<meta charset="utf-8">
<title>Maren Vickery — Business Cards</title>
<link rel="stylesheet" href="https://fonts.googleapis.com/css2?family=Mulish:wght@400;700&display=swap">
<style>
  :root {
    --backdrop: #4a1c38;
    --pink: #d9468f;
    --pink-light: #e46ea9;
    --pink-deep: #cc3a84;
    --ink: #2e2a2d;
    --ink-soft: #55505a;
    --charcoal: #34303a;
    --charcoal-deep: #26232b;
    --paper: #ffffff;
  }
  * { box-sizing: border-box; margin: 0; padding: 0; }
  html, body {
    width: 1200px;
    height: 876px;
    overflow: hidden;
    background: var(--backdrop);
    font-family: "Mulish", sans-serif;
  }
  .canvas {
    width: 1200px;
    height: 876px;
    display: flex;
    align-items: center;
    justify-content: center;
    gap: 60px;
  }
  .version {
    display: flex;
    flex-direction: column;
    align-items: center;
  }
  .card {
    position: relative;
    width: 520px;
    height: 297px;
    border-radius: 4px;
    overflow: hidden;
    box-shadow: 0 14px 30px rgba(0, 0, 0, 0.35);
  }

  /* Conservative version: contact side */
  .card--info { background: var(--paper); }
  .info-band {
    position: absolute;
    inset: 0;
    background: linear-gradient(120deg, var(--charcoal) 0%, var(--charcoal-deep) 100%);
    clip-path: polygon(66% 0, 100% 0, 100% 100%, 56% 100%);
  }
  .info-band-edge {
    position: absolute;
    inset: 0;
    background: var(--pink);
    clip-path: polygon(64.6% 0, 65.4% 0, 55.4% 100%, 54.6% 100%);
  }
  .contact {
    position: absolute;
    left: 30px;
    top: 28px;
    color: var(--ink);
    line-height: 1.25;
  }
  .contact-name { font-size: 19px; font-weight: 700; color: var(--pink-deep); }
  .contact-title, .contact-degrees { font-size: 11px; font-weight: 400; color: var(--ink-soft); }
  .contact-practice { font-size: 18px; font-weight: 400; margin-top: 12px; }
  .contact-details { list-style: none; font-size: 12px; margin-top: 14px; line-height: 1.4; color: var(--ink-soft); }
  .info-mark {
    position: absolute;
    right: 22px;
    top: 50%;
    transform: translateY(-50%);
    width: 170px;
  }

  /* Pink version: brand side */
  .card--brand {
    background: linear-gradient(120deg, var(--pink-light) 0%, var(--pink) 50%, var(--pink-deep) 100%);
  }
  .brand-mark {
    position: absolute;
    inset: 0;
    display: flex;
    align-items: center;
    justify-content: center;
  }

  /* Wordmark */
  .wordmark {
    display: flex;
    flex-direction: column;
    align-items: center;
    gap: 14px;
    color: var(--paper);
  }
  .wordmark-circle {
    width: 78px;
    height: 78px;
    border: 5px solid var(--paper);
    border-radius: 50%;
  }
  .wordmark-name {
    font-size: 13px;
    font-weight: 400;
    letter-spacing: 0.32em;
    text-transform: uppercase;
    white-space: nowrap;
  }
</style>
</head>
<body>
  <main class="canvas">
    <section class="version version--conservative" aria-label="Conservative version">
      <div class="card card--info" aria-label="Business card, contact side">
        <div class="info-band"></div>
        <div class="info-band-edge"></div>
        <div class="contact">
          <p class="contact-name">Maren Vickery</p>
          <p class="contact-title">Barrister &amp; Solicitor</p>
          <p class="contact-degrees">LL.B., B.C.L., B.F.A.</p>
          <p class="contact-practice">Criminal &amp; Immigration Law</p>
          <ul class="contact-details">
            <li>123 Harbour Bldg., Anywhere St.</li>
            <li>Toronto, ON 11001100</li>
            <li>000-000-0000</li>
            <li>000-000-0000</li>
            <li>Name@company.com</li>
          </ul>
        </div>
        <div class="info-mark">
          <div class="wordmark">
            <span class="wordmark-circle"></span>
            <span class="wordmark-name">Maren Vickery</span>
          </div>
        </div>
      </div>
    </section>

    <section class="version version--pink" aria-label="Pink version">
      <div class="card card--brand" aria-label="Business card, brand side">
        <div class="brand-mark">
          <div class="wordmark">
            <span class="wordmark-circle"></span>
            <span class="wordmark-name">Maren Vickery</span>
          </div>
        </div>
      </div>
    </section>
  </main>
</body>
</html>
```